Flyer Vacation Gift Certificate

I need to create a beautiful flyer 8.5 x 11 PDF format flyer design. <br/><br/>Instructions:<br/>The flyer will really be a gift voucher for a las vegas vacation getaway. So must have a Las Vegas Theme exciting fun<br/><br/>The voucher should have two modules that will be editable. <br/>Must have a "Compliments Of" area and also must have an "Exclusively For" area<br/><br/>Keep in mind that this flyer will be printed so keep that in mind :)<br/><br/>Here the is the content for the vacation voucher:<br/><br/>There is no doubt that Las Vegas is one of the hottest travel destinations around the world. In fact, some people would even go as far as<br/>saying that perhaps it is THE hottest place to visit. Enjoy up to 4 nights of resort/casino accommodations in exciting Las Vegas, NV. Millions of people travel to this exciting city each year to enjoy its thrills. Thanks to the business you received this certificate from, now you can enjoy exciting Las Vegas, NV too!<br/><br/>Features:<br/>*Travel 7 Days A Week<br/>*Stay Your Choice Of Nights (1-4 Nights)<br/>*Good For Two Adults & Two Children<br/>*Pay Just The Taxes & Fees<br/>*Multiple Travel Date Requests Allowed<br/>*Fully Transferable To Another Person<br/>*Just A 30 Days Advance Notice Required<br/>*You Will Have 12 Months To Complete Travel After Redemption<br/><br/>HOW CAN WE DO THIS?<br/><br/>We contract with the world leading hotel chains and resorts to help them fill their otherwise empty rooms.<br/><br/>We help fill empty rooms which the hotels, resorts and cruise lines turn into additional revenue from other areas of their property and future bookings.<br/><br/>Hotels rarely experience full occupancy, yet they remain open, providing rooms and services at fixed costs. So when hotels give out their rooms by partnering with marketing companies like us, they might miss out on the room fee, but they already didn't have that in the first place, at least now they have the opportunity to gain a customer for their in-house restaurants, room service, their casinos, an extra day stay, future bookings, etc.<br/><br/>VIEW ALL THE DETAILS OF THIS SPECIAL OFFER AND REDEEM ONLINE AT <br/>WWW.TOPAZVOUCHERDESK.COM<br/><br/>Certificate ID # 47261-38504<br/>Expires 02/29/2020<br/><br/><br/>*terms and conditions apply see website for details<br/><br/>KEEP IN MIND THE EXAMPLES I AM UPLOADING ARE SIMPLY TO SHOW YOU THAT THEY CONTAIN THE "COMPLIMENTS OF" AND "EXCLUSIVELY FOR" ELEMENTS. THESE MUST BE INCLUDED IN NEW DESIGN. PLEASE ONLY USE THE CONTENT I PROVIDED IN BRIEF, DONT USE CONTENT FROM EXAMPLES.

Target Market(s)

CONSUMERS THAT HAVE BEEN REWARDED WITH A VACATION CERTIFICATE FOR DOING BUSINESS WITH A COMPANY.

COMPANIES USE THESE AS MARKETING INCENTIVES TO ATTRACT MORE CUSTOMERS AND TO REWARD LOYALTY, ETC.

Industry/Entity Type

Travel Industry

Colors

Designer to choose colors to be used in the design.

Requirements
Must have
• I need to create a beautiful flyer 8.5 x 11 PDF format flyer design.
• Instructions:
• The flyer will really be a gift voucher for a las vegas vacation getaway. So must have a Las Vegas Theme exciting fun
• The voucher should have two modules that will be editable.
• Must have a "Compliments Of" area and also must have an "Exclusively For" area
• Keep in mind that this flyer will be printed so keep that in mind :)
• Here the is the content for the vacation voucher:
• There is no doubt that Las Vegas is one of the hottest travel destinations around the world. In fact, some people would even go as far as
• saying that perhaps it is THE hottest place to visit. Enjoy up to 4 nights of resort/casino accommodations in exciting Las Vegas, NV. Millions of people travel to this exciting city each year to enjoy its thrills. Thanks to the business you received this certificate from, now you can enjoy exciting Las Vegas, NV too!
• Features:
• *Travel 7 Days A Week
• *Stay Your Choice Of Nights (1-4 Nights)
• *Good For Two Adults & Two Children
• *Pay Just The Taxes & Fees
• *Multiple Travel Date Requests Allowed
• *Fully Transferable To Another Person
• *Just A 30 Days Advance Notice Required
• *You Will Have 12 Months To Complete Travel After Redemption
• HOW CAN WE DO THIS?
• We contract with the world leading hotel chains and resorts to help them fill their otherwise empty rooms.
• We help fill empty rooms which the hotels, resorts and cruise lines turn into additional revenue from other areas of their property and future bookings.
• Hotels rarely experience full occupancy, yet they remain open, providing rooms and services at fixed costs. So when hotels give out their rooms by partnering with marketing companies like us, they might miss out on the room fee, but they already didn't have that in the first place, at least now they have the opportunity to gain a customer for their in-house restaurants, room service, their casinos, an extra day stay, future bookings, etc.
• VIEW ALL THE DETAILS OF THIS SPECIAL OFFER AND REDEEM ONLINE AT
• WWW.TOPAZVOUCHERDESK.COM
• Certificate ID # 47261-38504
• Expires 02/29/2020
• *terms and conditions apply see website for details
• KEEP IN MIND THE EXAMPLES I AM UPLOADING ARE SIMPLY TO SHOW YOU THAT THEY CONTAIN THE "COMPLIMENTS OF" AND "EXCLUSIVELY FOR" ELEMENTS. THESE MUST BE INCLUDED IN NEW DESIGN. PLEASE ONLY USE THE CONTENT I PROVIDED IN BRIEF, DONT USE CONTENT FROM EXAMPLES.
Nice to have
• EXCITING LAS VEGAS IMAGES THAT MAKE SOMEONE WANT TO GO THERE

```html
<!DOCTYPE html>
<html lang="en">
<head>
<meta charset="utf-8">
<title>Airfare &amp; Hotel For Two – Las Vegas Vacation Certificate</title>
<link href="https://fonts.googleapis.com/css2?family=Montserrat:wght@300;400;500;600;700&display=swap" rel="stylesheet">
<style>
  :root {
    --sky-top: #3f78c4;
    --sky-mid: #8fb3dd;
    --sky-low: #d9e4ef;
    --brand-blue: #2f69ad;
    --band-blue: #4a7fc1;
    --alert-red: #f01414;
    --panel-grey: #e6e7e9;
    --column-grey: #bfc0cb;
    --navy: #141d4a;
    --text-grey: #8a8c8f;
    --body-dark: #3a3c40;
    --ink: #111111;
    --white: #ffffff;
  }
  * { margin: 0; padding: 0; box-sizing: border-box; }
  html, body { width: 944px; height: 1200px; overflow: hidden; background: var(--white); }
  body { font-family: "Montserrat", Arial, sans-serif; color: var(--ink); }
  .certificate { position: relative; width: 944px; height: 1200px; overflow: hidden; }

  .hero-photo {
    position: absolute; left: 0; top: 0; width: 944px; height: 357px;
    background:
      radial-gradient(ellipse 70% 30% at 50% 100%, #f2f4f7 0%, rgba(242,244,247,0) 70%),
      linear-gradient(180deg, var(--sky-top) 0%, var(--sky-mid) 45%, var(--sky-low) 100%);
  }

  .compliments {
    position: absolute; left: 655px; top: 0; width: 260px; height: 223px;
    background: var(--white); text-align: center;
  }
  .compliments-title {
    margin-top: 20px; font-size: 19.5px; font-weight: 500; line-height: 24px;
    letter-spacing: 1.2px; color: var(--brand-blue);
  }
  .sponsor-name {
    display: flex; align-items: center; justify-content: center; gap: 7px;
    margin-top: 14px; font-size: 22px; font-weight: 600; color: var(--brand-blue);
  }
  .sponsor-mark { width: 14px; height: 14px; background: var(--alert-red); }
  .sponsor-lines { margin-top: 15px; font-size: 16px; line-height: 26px; letter-spacing: 0.4px; }

  .exclusively {
    position: absolute; left: 0; top: 258px; width: 378px; height: 28px;
    background: var(--alert-red); color: var(--white);
    font-size: 15.5px; font-weight: 500; letter-spacing: 0.8px; line-height: 28px; padding-left: 38px;
  }
  .title-band { position: absolute; left: 0; top: 288px; }
  .title-band h1 {
    position: absolute; left: 36px; top: 12px; white-space: nowrap;
    font-size: 42px; font-weight: 600; letter-spacing: 2px; color: var(--white); line-height: 46px;
  }

  .intro {
    position: absolute; left: 38px; top: 368px; width: 866px; height: 85px;
    background: var(--panel-grey); padding: 9px 9px;
    font-size: 12.5px; font-weight: 300; line-height: 17px; letter-spacing: 0.15px; color: var(--text-grey);
  }

  .terms-band { position: absolute; left: 0; top: 465px; }
  .terms-band h2 {
    position: absolute; left: 32px; top: 7px; white-space: nowrap;
    font-size: 23px; font-weight: 500; letter-spacing: 1.5px; color: var(--white); line-height: 28px;
  }
  .terms {
    position: absolute; left: 38px; top: 518px; width: 866px; height: 269px;
    background: var(--panel-grey); padding: 8px 9px;
    font-size: 10.5px; font-weight: 300; line-height: 13.75px; color: var(--text-grey);
  }

  .redeem-panel, .payment-panel {
    position: absolute; top: 800px; height: 400px; background: var(--panel-grey);
  }
  .redeem-panel { left: 0; width: 326px; padding: 18px 22px 0 23px; }
  .payment-panel { left: 619px; width: 325px; padding: 18px 20px 0 19px; }
  .shipping-panel {
    position: absolute; left: 348px; top: 836px; width: 249px; height: 364px;
    background: var(--column-grey); padding: 14px 12px 0 10px;
  }
  .panel-heading { font-size: 15.5px; font-weight: 500; letter-spacing: 0.6px; line-height: 20px; }
  .redeem-panel .panel-heading { letter-spacing: 0.2px; }
  .payment-panel .panel-heading { letter-spacing: 1px; }
  .column-frame { position: absolute; left: 0; top: 0; }

  .panel-body { margin-top: 14px; font-size: 11px; line-height: 15px; color: var(--body-dark); }
  .redeem-step { margin-bottom: 14px; }
  .step-label { display: block; font-weight: 600; color: var(--brand-blue); font-size: 12px; margin-bottom: 3px; }
  .site-address { display: block; margin-top: 4px; font-weight: 700; font-size: 13px; color: var(--alert-red); letter-spacing: 0.3px; }
  .certificate-id { margin-top: 22px; font-weight: 600; font-size: 12.5px; color: var(--ink); }
  .expires { margin-top: 3px; font-weight: 600; font-size: 12.5px; color: var(--alert-red); }
  .fine-print { margin-top: 14px; font-size: 9.5px; font-style: italic; color: var(--text-grey); }

  .feature-list { list-style: none; margin-top: 14px; }
  .feature-list li {
    position: relative; padding-left: 18px; margin-bottom: 11px;
    font-size: 11.5px; line-height: 15px; font-weight: 500; color: var(--navy);
  }
  .feature-list svg { position: absolute; left: 0; top: 2px; }

  .how-heading { margin-top: 14px; font-size: 12px; font-weight: 600; color: var(--brand-blue); letter-spacing: 0.4px; }
  .how-text { margin-top: 7px; font-size: 10.5px; line-height: 14.5px; font-weight: 400; color: var(--body-dark); }
</style>
</head>
<body>
<main class="certificate">
  <div class="hero-photo" role="img" aria-label="Photo of a white passenger jet flying above clouds in a blue sky, heading to Las Vegas"></div>

  <aside class="compliments">
    <p class="compliments-title">THIS CERTIFICATE IS<br>COMPLIMENTS OF</p>
    <p class="sponsor-name"><span class="sponsor-mark"></span>TextLane Pro</p>
    <p class="sponsor-lines">Certificate Courtesy Of<br>Text Line 2<br>Text Line 3</p>
  </aside>

  <div class="exclusively">EXCLUSIVELY FOR : CUSTOMER NAME</div>

  <div class="title-band">
    <svg width="740" height="69" viewBox="0 0 740 69" aria-hidden="true">
      <polygon points="0,0 704,0 736,34.5 704,69 0,69" fill="var(--band-blue)"/>
    </svg>
    <h1>AIRFARE &amp; HOTEL FOR TWO</h1>
  </div>

  <p class="intro">There is no doubt that Las Vegas is one of the hottest travel destinations around the world. In fact, some people would even go as far as saying that perhaps it is THE hottest place to visit. Enjoy up to 4 nights of resort/casino accommodations in exciting Las Vegas, NV. Millions of people travel to this exciting city each year to enjoy its thrills. Thanks to the business you received this certificate from, now you can enjoy exciting Las Vegas, NV too!</p>

  <div class="terms-band">
    <svg width="944" height="42" viewBox="0 0 944 42" aria-hidden="true">
      <line x1="330" y1="21" x2="944" y2="21" stroke="var(--band-blue)" stroke-width="1"/>
      <polygon points="0,0 316,0 336,21 316,42 0,42" fill="var(--band-blue)"/>
    </svg>
    <h2>TERMS &amp; CONDITIONS</h2>
  </div>

  <p class="terms">This certificate will be considered void if bartered or purchased for legal tender by the recipient. This certificate is valid for a reservation request form offering 2 adults 21 years of age and older plus up to 2 children under the age of 18, up to 4 nights of hotel/resort accommodations in Las Vegas, NV. The cost to activate this certificate to receive the reservation request form is just a one-time non-refundable $15.95 processing fee. The cost upon requesting reservations is just a tax &amp; fee deposit of $33 per night. Taxes &amp; fees usually range from $12-$33 per night depending on the time of the year travel happens. If the taxes &amp; fees are less than the $33 per night the difference will be refunded after travel is completed. 30 days advance notice is required. In order to guarantee that you will show up to your booked reservation you will be required to pay a REFUNDABLE $50 "Reservation Guarantee Deposit". If you send in your travel dates, etc and you do not end up traveling then the reservation guarantee deposit will not be refundable. Dates 7 days before and after holidays and conventions are not available. This offer is valid 7 days a week and subject to availability. Friday and Saturday nights will require a surcharge of $20 per night. A $5 per person per night surcharge is enforced for each child up to 2 children under the age of 18. This offer is not valid for group travel. This offer is only good for U.S. and Canadian residents only. The recipient of this certificate is responsible for all expenses including but not limited to: transfers, food, gratuities, hotel surcharges, resort fees and any other miscellaneous expenses. If you activate this certificate online you will be able to instantly print your reservation request form. This certificate cannot be combined with any other promotional vacation offer. The expiration date on this certificate pertains only to activation of this certificate and not actual travel. You must activate this certificate by the expiration date printed on this certificate in order to access the reservation request form. You must fill out the reservation request form with your destination choices and arrival dates and mail it to our fulfillment department within 6 months after activation, however travel can be completed within 12 months after activation. You will be required to give the travel agency multiple arrival dates and destinations. Only one Las Vegas certificate Per Household Per Year. This certificate has no cash surrender value, void if discontinued and where prohibited by law. The terms of this offer are subject to change without notice. Do not rely upon representations other than what is printed on this certificate or the reservation request form. CST # 5830417</p>

  <section class="redeem-panel">
    <h3 class="panel-heading">2 Ways To Redeem:</h3>
    <div class="panel-body">
      <p class="redeem-step"><span class="step-label">1. Online</span>VIEW ALL THE DETAILS OF THIS SPECIAL OFFER AND REDEEM ONLINE AT <span class="site-address">WWW.TOPAZVOUCHERDESK.COM</span></p>
      <p class="redeem-step"><span class="step-label">2. By Mail</span>Fill out the reservation request form with your destination choices and arrival dates and mail it to our fulfillment department.</p>
      <p class="certificate-id">Certificate ID # 47261-38504</p>
      <p class="expires">Expires 02/29/2020</p>
      <p class="fine-print">*terms and conditions apply see website for details</p>
    </div>
  </section>

  <svg class="column-frame" width="944" height="1200" viewBox="0 0 944 1200" aria-hidden="true">
    <polygon points="326,800 348,836 348,1200 326,1200" fill="var(--navy)"/>
    <polygon points="619,800 597,836 597,1200 619,1200" fill="var(--navy)"/>
  </svg>

  <section class="shipping-panel">
    <h3 class="panel-heading">SHIPPING INFORMATION</h3>
    <ul class="feature-list">
      <li><svg width="11" height="11" viewBox="0 0 11 11" aria-hidden="true"><polyline points="1,6 4,9 10,2" fill="none" stroke="var(--alert-red)" stroke-width="2"/></svg>Travel 7 Days A Week</li>
      <li><svg width="11" height="11" viewBox="0 0 11 11" aria-hidden="true"><polyline points="1,6 4,9 10,2" fill="none" stroke="var(--alert-red)" stroke-width="2"/></svg>Stay Your Choice Of Nights (1-4 Nights)</li>
      <li><svg width="11" height="11" viewBox="0 0 11 11" aria-hidden="true"><polyline points="1,6 4,9 10,2" fill="none" stroke="var(--alert-red)" stroke-width="2"/></svg>Good For Two Adults &amp; Two Children</li>
      <li><svg width="11" height="11" viewBox="0 0 11 11" aria-hidden="true"><polyline points="1,6 4,9 10,2" fill="none" stroke="var(--alert-red)" stroke-width="2"/></svg>Pay Just The Taxes &amp; Fees</li>
      <li><svg width="11" height="11" viewBox="0 0 11 11" aria-hidden="true"><polyline points="1,6 4,9 10,2" fill="none" stroke="var(--alert-red)" stroke-width="2"/></svg>Multiple Travel Date Requests Allowed</li>
      <li><svg width="11" height="11" viewBox="0 0 11 11" aria-hidden="true"><polyline points="1,6 4,9 10,2" fill="none" stroke="var(--alert-red)" stroke-width="2"/></svg>Fully Transferable To Another Person</li>
      <li><svg width="11" height="11" viewBox="0 0 11 11" aria-hidden="true"><polyline points="1,6 4,9 10,2" fill="none" stroke="var(--alert-red)" stroke-width="2"/></svg>Just A 30 Days Advance Notice Required</li>
      <li><svg width="11" height="11" viewBox="0 0 11 11" aria-hidden="true"><polyline points="1,6 4,9 10,2" fill="none" stroke="var(--alert-red)" stroke-width="2"/></svg>You Will Have 12 Months To Complete Travel After Redemption</li>
    </ul>
  </section>

  <section class="payment-panel">
    <h3 class="panel-heading">PAYMENT INFORMATION</h3>
    <p class="how-heading">HOW CAN WE DO THIS?</p>
    <p class="how-text">We contract with the world leading hotel chains and resorts to help them fill their otherwise empty rooms.</p>
    <p class="how-text">We help fill empty rooms which the hotels, resorts and cruise lines turn into additional revenue from other areas of their property and future bookings.</p>
    <p class="how-text">Hotels rarely experience full occupancy, yet they remain open, providing rooms and services at fixed costs. So when hotels give out their rooms by partnering with marketing companies like us, they might miss out on the room fee, but they already didn't have that in the first place, at least now they have the opportunity to gain a customer for their in-house restaurants, room service, their casinos, an extra day stay, future bookings, etc.</p>
  </section>
</main>
</body>
</html>
```